KRL Banner Logo with Rocky Mountain of CO as the background

I need a banner/logo for my KRL year. So have a banner design that is like an intentional path or inspiring.

• KRL Silver Ridge CO mountain as background and they may add similar images that I sent you
• Wording: Intentional Path
Learning year 2025-2026
• Add the KRL logo (the white and blue image – you will see these online)

UPDATE: Attached are example images on how we envision the banner. Please do not use the attached example sample images. Kindly look for similar looking images that are FREE TO USE Commercially.

CEO, top executives

0054AA
0677BA
7BADD7
CADEEF
E8F1F8

• • KRL Silver Ridge CO mountain as background and they may add similar images that I sent you • Wording: Intentional Path Learning year 2025-2026 • Add the KRL logo (the white and blue image – you will see these online)
• It has nice to have the inspirational images attached but you can have your own design. This is only for sample.

```html
<!DOCTYPE html>
<html lang="en">
<head>
<meta charset="utf-8">
<title>KRL Silver Ridge – Intentional Path Banner</title>
<link rel="stylesheet" href="https://fonts.googleapis.com/css2?family=Alfa+Slab+One&family=Poppins:wght@400;600;700&display=swap">
<style>
  :root {
    --page: #ffffff;
    --sky: #cadeef;
    --wave: #7badd7;
    --wave-deep: #0677ba;
    --navy: #0054aa;
    --ink: #0a3f7e;
    --mist: #e8f1f8;
    --frame: rgba(255, 255, 255, 0.8);
    --peak-warm: #d9a23a;
    --peak-green: #7d8a2c;
    --peak-shadow: #5a4a3c;
  }
  html, body {
    margin: 0;
    padding: 0;
    width: 1200px;
    height: 1000px;
    overflow: hidden;
    background: var(--page);
  }
  .canvas {
    position: relative;
    width: 1200px;
    height: 1000px;
  }
  .banner {
    position: absolute;
    left: 75px;
    top: 299px;
    width: 1060px;
    height: 403px;
    overflow: hidden;
    background: var(--sky);
  }
  .banner-shapes {
    position: absolute;
    inset: 0;
    width: 1060px;
    height: 403px;
  }
  .brand {
    position: absolute;
    left: 206px;
    top: 36px;
    display: flex;
    align-items: center;
    gap: 10px;
    font-family: "Poppins", sans-serif;
    font-weight: 400;
    font-size: 34px;
    letter-spacing: 1px;
    color: var(--ink);
    line-height: 1;
  }
  .brand-mark {
    width: 26px;
    height: 26px;
    background: var(--ink);
  }
  .chapter-name {
    position: absolute;
    right: 192px;
    top: 33px;
    margin: 0;
    font-family: "Poppins", sans-serif;
    font-weight: 700;
    font-size: 11px;
    line-height: 1;
    color: var(--ink);
  }
  .headline {
    position: absolute;
    right: 180px;
    top: 172px;
    margin: 0;
    font-family: "Alfa Slab One", serif;
    font-weight: 400;
    font-size: 42px;
    letter-spacing: 2px;
    color: var(--navy);
    text-shadow: 3px 3px 0 var(--mist);
    line-height: 1;
    white-space: nowrap;
  }
  .subline {
    position: absolute;
    right: 184px;
    top: 238px;
    margin: 0;
    font-family: "Poppins", sans-serif;
    font-weight: 600;
    font-size: 20px;
    color: var(--ink);
    line-height: 1;
    white-space: nowrap;
  }
  .social-list {
    position: absolute;
    left: 721px;
    top: 327px;
    display: flex;
    gap: 36px;
    margin: 0;
    padding: 0;
    list-style: none;
  }
  .social-item {
    width: 48px;
    height: 48px;
    border-radius: 50%;
    background: var(--mist);
  }
</style>
</head>
<body>
<div class="canvas">
  <section class="banner">
    <svg class="banner-shapes" viewBox="0 0 1060 403" xmlns="http://www.w3.org/2000/svg">
      <defs>
        <linearGradient id="peak-tones" x1="0" y1="0" x2="1" y2="1">
          <stop offset="0" stop-color="var(--peak-shadow)"/>
          <stop offset="0.35" stop-color="var(--peak-warm)"/>
          <stop offset="0.7" stop-color="var(--peak-green)"/>
          <stop offset="1" stop-color="var(--peak-shadow)"/>
        </linearGradient>
      </defs>
      <path class="wave-top" fill="var(--wave)"
            d="M355,0 L900,0 C930,40 940,90 890,112 C820,140 760,92 660,116 C570,140 440,140 380,92 C340,58 345,22 355,0 Z"/>
      <path class="wave-dark" fill="var(--navy)"
            d="M898,0 L1060,0 L1060,403 L325,403 C335,330 372,302 460,300 C560,298 600,272 720,267 C820,263 900,302 950,282 C995,262 955,205 942,152 C930,100 985,62 898,0 Z"/>
      <path class="wave-side" fill="var(--wave-deep)"
            d="M1060,112 C1000,112 958,152 950,202 C944,252 984,292 1060,298 Z"/>
      <path class="mountain-photo" role="img" aria-label="Photo of a sunlit mountain ridge with grassy slopes at sunrise"
            fill="url(#peak-tones)"
            d="M15,40 C60,28 160,24 188,56 C212,86 220,140 258,176 C292,206 330,210 372,222 C408,236 428,270 425,300 C380,310 350,340 330,389 L15,389 Z"/>
      <rect class="inner-frame" x="14" y="14" width="1032" height="375" fill="none" stroke="var(--frame)" stroke-width="1.5"/>
    </svg>

    <div class="brand"><span class="brand-mark"></span>KRL</div>
    <p class="chapter-name">KRL Gold Silver Ridge Chapter</p>
    <h1 class="headline">INTENTIONAL PATH</h1>
    <p class="subline">2025-2026 Learning year</p>
    <ul class="social-list" aria-label="Social channels">
      <li class="social-item"></li>
      <li class="social-item"></li>
      <li class="social-item"></li>
      <li class="social-item"></li>
    </ul>
  </section>
</div>
</body>
</html>
```